Business Card Design needed for logo design project

This project is linked to Logo: brand identity for modern furniture design studio..

Our company needs a Business Card Design. Please refer to our original project in the link above.

Industry/Entity Type

Business

```html
<!DOCTYPE html>
<html lang="en">
<head>
<meta charset="utf-8">
<title>Vellum — Business Card</title>
<link rel="stylesheet" href="https://fonts.googleapis.com/css2?family=Open+Sans:wght@300;400;600&display=swap">
<style>
  :root {
    --backdrop: #e9e6e1;
    --card-dark: #2a2a2a;
    --card-light: #ffffff;
    --ink: #222222;
    --ink-soft: #555555;
    --rule: #8a8a8a;
    --band: #2e2e2e;
    --band-text: #f2f2f2;
  }
  * { margin: 0; padding: 0; box-sizing: border-box; }
  html, body {
    width: 1200px;
    height: 1023px;
    overflow: hidden;
    background: var(--backdrop);
    font-family: "Open Sans", Arial, sans-serif;
  }
  .stage {
    position: relative;
    width: 1200px;
    height: 1023px;
  }
  .card {
    position: absolute;
    left: 250px;
    width: 700px;
    height: 400px;
    box-shadow: 0 6px 18px rgba(0,0,0,0.18);
  }
  .card-back {
    top: 70px;
    background: var(--card-dark);
    display: flex;
    align-items: center;
    justify-content: center;
  }
  .card-back .wordmark {
    color: var(--card-light);
    font-size: 96px;
  }
  .wordmark {
    font-family: "Open Sans", Arial, sans-serif;
    font-weight: 300;
    letter-spacing: 1px;
    line-height: 1;
  }
  .card-front {
    top: 530px;
    background: var(--card-light);
  }
  .card-front .wordmark {
    position: absolute;
    left: 55px;
    top: 160px;
    font-size: 86px;
    color: var(--ink);
  }
  .divider {
    position: absolute;
    left: 343px;
    top: 128px;
    width: 2px;
    height: 162px;
    background: var(--rule);
  }
  .contact {
    position: absolute;
    left: 372px;
    top: 134px;
    color: var(--ink);
  }
  .contact .name {
    font-size: 27px;
    font-weight: 400;
    line-height: 1.1;
  }
  .contact .role {
    font-size: 17px;
    color: var(--ink-soft);
    margin-bottom: 24px;
  }
  .contact .details {
    list-style: none;
    font-size: 17px;
    line-height: 1.3;
    color: var(--ink-soft);
  }
  .contact .details .label {
    color: var(--ink);
    font-weight: 600;
  }
  .tagline-band {
    position: absolute;
    left: 0;
    bottom: 0;
    width: 100%;
    height: 48px;
    background: var(--band);
    color: var(--band-text);
    font-size: 17px;
    display: flex;
    align-items: center;
    justify-content: center;
  }
</style>
</head>
<body>
  <main class="stage">
    <section class="card card-back" aria-label="Card back">
      <span class="wordmark">vellum</span>
    </section>

    <section class="card card-front" aria-label="Card front">
      <span class="wordmark">vellum</span>
      <div class="divider"></div>
      <div class="contact">
        <p class="name">Mark Alden Reyes</p>
        <p class="role">general manager</p>
        <ul class="details">
          <li><span class="label">phone:</span> +01 555 0142</li>
          <li><span class="label">email:</span> markreyes@vellummail.com</li>
          <li><span class="label">website:</span> www.vellumstudio.com</li>
        </ul>
      </div>
      <div class="tagline-band">this area can be a tagline or company location address</div>
    </section>
  </main>
</body>
</html>
```